Tall Fern Software

We are a software company selling endpoint visibility, access and security technology to enterprise-level IT departments.

Our technology helps organizations gain comprehensive visibility into and control over devices accessing their corporate network so they can quickly identify and address suspicious activity on the network that could lead to potential threats like data breaches.

This technology can cost organizations upwards of $1M - depending on the size of the organization. Our primary clients are Pinnacle 2,000 companies.

We want a professional, polished business card to represent our new brand.

Info fields to include on the card:
Name
Job Title
Office Phone #
Cell Phone #
Email address
Address: 4217 Westbrook Ridge Blvd., Ste. 2600, Riverton, MN 55918
Website address: www.tallfernsoftware.example
Tagline: Discover the edge. Optimize the whole.

Logo files and color specs document are attached. Would like color scheme to coordinate with the logo.

Also looking at stationary/envelope designs in conjunction with the business card designs. Received very few designs that included the stationary.

```html
<!DOCTYPE html>
<html lang="en">
<head>
<meta charset="utf-8">
<title>Tall Fern Software – Business Card</title>
<link rel="stylesheet" href="https://fonts.googleapis.com/css2?family=Montserrat:wght@400;500;700&display=swap">
<style>
  :root {
    --stage: #ece8e4;
    --wine-light: #a4464a;
    --wine: #7a1c20;
    --wine-dark: #4e0a0d;
    --paper: #ffffff;
    --band: #dcdcdc;
    --ink: #6a6a6a;
    --ink-soft: #8c8c8c;
    --logo-ink: #ffffff;
  }
  * { box-sizing: border-box; margin: 0; padding: 0; }
  html, body { width: 1200px; height: 913px; overflow: hidden; }
  body {
    background: var(--stage);
    font-family: "Montserrat", sans-serif;
    position: relative;
  }
  .card {
    position: absolute;
    width: 500px;
    height: 286px;
    border-radius: 4px;
    overflow: hidden;
    box-shadow: 0 6px 18px rgba(0,0,0,.18);
  }
  .card-front {
    left: 70px; top: 314px;
    background: linear-gradient(160deg, var(--wine-light) 0%, var(--wine) 45%, var(--wine-dark) 100%);
    display: flex; align-items: center; justify-content: center;
  }
  .card-back { left: 630px; top: 314px; background: var(--paper); }
  .card-back .backdrop { position: absolute; inset: 0; }

  .wordmark {
    display: flex; align-items: center; gap: 12px;
    color: var(--logo-ink);
    font-weight: 700;
    letter-spacing: 2px;
    text-transform: uppercase;
  }
  .wordmark .dot {
    width: 12px; height: 12px; border-radius: 50%;
    background: var(--logo-ink);
    flex: none;
  }
  .card-front .wordmark { font-size: 26px; }
  .card-back .wordmark {
    position: absolute; left: 28px; top: 160px;
    font-size: 15px; line-height: 1.3; letter-spacing: 1.5px; gap: 10px;
  }
  .card-back .wordmark .dot { width: 9px; height: 9px; }

  .holder { position: absolute; left: 248px; top: 38px; }
  .holder .name { font-size: 13px; font-weight: 700; color: var(--ink); letter-spacing: 1px; }
  .holder .title { font-size: 9px; color: var(--ink-soft); margin-top: 3px; }

  .address {
    position: absolute; left: 300px; top: 122px;
    font-size: 8.5px; line-height: 1.45; color: var(--ink);
  }
  .contacts {
    position: absolute; left: 300px; top: 170px;
    list-style: none; font-size: 8.5px; color: var(--ink);
  }
  .contacts li { display: flex; align-items: center; gap: 6px; line-height: 1.75; }
  .contacts svg { width: 9px; height: 9px; fill: var(--wine); flex: none; }
</style>
</head>
<body>

  <section class="card card-front" aria-label="Card front">
    <div class="wordmark"><span class="dot"></span>Tall Fern Software</div>
  </section>

  <section class="card card-back" aria-label="Card back">
    <svg class="backdrop" viewBox="0 0 500 286" preserveAspectRatio="none" aria-hidden="true">
      <defs>
        <linearGradient id="wineFill" x1="0" y1="0" x2="1" y2="1">
          <stop offset="0" stop-color="#7a1c20"/>
          <stop offset="0.6" stop-color="#8e2a2e"/>
          <stop offset="1" stop-color="#4e0a0d"/>
        </linearGradient>
      </defs>
      <path d="M0 0 H222 C200 120 262 220 330 286 H0 Z" fill="#dcdcdc"/>
      <path d="M0 0 H210 C186 120 246 220 312 286 H0 Z" fill="url(#wineFill)"/>
    </svg>

    <div class="wordmark"><span class="dot"></span><span>Tall Fern<br>Software</span></div>

    <div class="holder">
      <p class="name">YOUR NAME</p>
      <p class="title">Title</p>
    </div>

    <p class="address">4217 Westbrook Ridge Blvd.<br>Ste. 2600, Riverton, MN 55918</p>

    <ul class="contacts">
      <li><svg viewBox="0 0 10 10"><rect x="2.5" y="0" width="5" height="10" rx="1"/></svg>00.123.123.123.123</li>
      <li><svg viewBox="0 0 10 10"><path d="M1 4 C1 1 9 1 9 4 L7 4 L7 3 L3 3 L3 4 Z M2 5 H8 L9 10 H1 Z"/></svg>00.00.00.0000</li>
      <li><svg viewBox="0 0 10 10"><path d="M0 2 H10 V8 H0 Z M0 2 L5 6 L10 2" stroke="#fff" stroke-width=".8"/></svg>yourname@tallfernsoftware.example</li>
      <li><svg viewBox="0 0 10 10"><circle cx="5" cy="5" r="5"/><path d="M0 5 H10 M5 0 V10" stroke="#fff" stroke-width=".7"/></svg>www.tallfernsoftware.example</li>
    </ul>
  </section>

</body>
</html>
```